Advertising poster for podcast event

"The Lantern Table" is one of the most popular podcasts in Switzerland (https://listen.harbofeed.example/show/4kqpVXRT219LmNaw8BYdE5). It is hosted by the two radio DJs Lukas Brenner and Rafael Tanner. For a series of live shows where the podcast is recorded with an audience, we need a design of a poster. This should have the format A3 high. In addition, the image must be used that was uploaded here, because this is the cover photo with which you can always recognize the podcast. But what is designed around it is up to you. In addition, it must contain the following text:

- Title of the event:
The lantern table - Live
- Show dates:
Saturday, November 11, 2023 - Solothurn
Wednesday, December 27, 2023 - Berne
Thursday, December 28, 2023 - Berne
- A line with additional information about the presale:
The Dome, information and tickets: www.kuppelfest.example

Target Market(s)

Switzerland

Industry/Entity Type

Entertainment

Requirements
Must have
• The attached image and text according to the briefing.

```html
<!DOCTYPE html>
<html lang="en">
<head>
<meta charset="utf-8">
<title>The Lantern Table Live – Poster</title>
<link rel="stylesheet" href="https://fonts.googleapis.com/css2?family=Montserrat:wght@500;700;800&family=Poppins:wght@600;700;800&display=swap">
<style>
  :root {
    --red: #f40000;
    --black: #0b0b0b;
    --white: #ffffff;
    --ink: #1a1a1a;
    --backdrop: #e9e9e9;
  }
  * { margin: 0; padding: 0; box-sizing: border-box; }
  html, body { width: 900px; height: 1200px; overflow: hidden; background: var(--backdrop); }
  .poster {
    position: absolute; left: 26px; top: 0;
    width: 848px; height: 1200px;
    background: var(--white);
    font-family: "Montserrat", sans-serif;
  }
  .sunburst {
    position: absolute; left: 6px; top: 16px; width: 836px; height: 822px;
    background: radial-gradient(circle at 50% 45%, #ffffff 0%, #ffd6d6 22%, #ff4a4a 55%, var(--red) 100%);
  }
  .hosts-art {
    position: absolute; left: 133px; top: 240px; width: 582px; height: 400px;
    background: linear-gradient(180deg, #d9a88a 0%, #6b6b6b 55%, #111111 100%);
    border-radius: 4px;
  }
  .title-card {
    position: absolute; left: 92px; top: 638px; width: 666px; height: 221px;
    background: var(--white); border-radius: 16px;
    box-shadow: 0 8px 14px rgba(0,0,0,.18);
    display: flex; flex-direction: column; align-items: center; justify-content: center;
    gap: 10px;
  }
  .title {
    font-family: "Poppins", sans-serif; font-weight: 800; font-size: 54px;
    line-height: 1; color: var(--red); letter-spacing: -1px; white-space: nowrap;
  }
  .live {
    font-family: "Poppins", sans-serif; font-weight: 700; font-size: 22px;
    letter-spacing: 10px; color: var(--ink); padding-left: 10px;
  }
  .hosted-by {
    position: absolute; left: 0; right: 0; top: 896px; text-align: center;
    font-size: 12px; font-weight: 500; letter-spacing: 6px; color: var(--ink);
  }
  .host-names {
    position: absolute; left: 0; right: 0; top: 914px; text-align: center;
    font-size: 13px; font-weight: 800; letter-spacing: 7px; color: var(--red);
  }
  .show-date {
    position: absolute; top: 965px; height: 112px;
    border: 2px solid var(--red); background: var(--white);
  }
  .show-date .date-head {
    height: 74px; background: var(--red); color: var(--white);
    font-family: "Poppins", sans-serif; position: relative;
  }
  .day-num { position: absolute; left: 12px; top: 2px; font-size: 46px; font-weight: 800; line-height: 1.1; letter-spacing: -2px; }
  .month { position: absolute; right: 12px; top: 8px; font-size: 11px; font-weight: 700; line-height: 1; }
  .year { position: absolute; right: 12px; top: 18px; font-size: 29px; font-weight: 800; line-height: 1; }
  .weekday {
    position: absolute; left: 12px; right: 12px; top: 56px; height: 12px;
    background: var(--white); color: var(--red);
    font-family: "Montserrat", sans-serif; font-size: 9px; font-weight: 500;
    letter-spacing: 7px; text-align: center; line-height: 12px;
  }
  .city {
    text-align: center; font-family: "Poppins", sans-serif; font-weight: 700;
    font-size: 19px; letter-spacing: 4px; color: var(--red); line-height: 34px;
  }
  .presale-info {
    position: absolute; left: 0; right: 0; top: 1118px; text-align: center;
    font-size: 12px; font-weight: 500; letter-spacing: 7px; color: var(--ink);
  }
  .presale-url {
    position: absolute; left: 0; right: 0; top: 1138px; text-align: center;
    font-size: 18px; font-weight: 800; letter-spacing: 8px; color: var(--red);
  }
</style>
</head>
<body>
<main class="poster">
  <div class="sunburst" role="img" aria-label="Red and white sunburst rays with halftone dots radiating from behind the hosts"></div>
  <div class="hosts-art" role="img" aria-label="Podcast cover illustration: the two hosts with a vintage microphone between stacked loudspeakers"></div>

  <section class="title-card">
    <h1 class="title">THE LANTERN TABLE</h1>
    <p class="live">LIVE</p>
  </section>

  <p class="hosted-by">HOSTED BY</p>
  <p class="host-names">LUKAS BRENNER &amp; RAFAEL TANNER</p>

  <article class="show-date" style="left:68px;width:207px">
    <div class="date-head">
      <span class="day-num">11TH</span>
      <span class="month">NOVEMBER</span>
      <span class="year">2023</span>
      <span class="weekday">SATURDAY</span>
    </div>
    <p class="city">SOLOTHURN</p>
  </article>
  <article class="show-date" style="left:303px;width:225px">
    <div class="date-head">
      <span class="day-num">27TH</span>
      <span class="month">DECEMBER</span>
      <span class="year">2023</span>
      <span class="weekday">WEDNESDAY</span>
    </div>
    <p class="city">BERNE</p>
  </article>
  <article class="show-date" style="left:557px;width:225px">
    <div class="date-head">
      <span class="day-num">28TH</span>
      <span class="month">DECEMBER</span>
      <span class="year">2023</span>
      <span class="weekday">THURSDAY</span>
    </div>
    <p class="city">BERNE</p>
  </article>

  <p class="presale-info">THE DOME, INFORMATION AND TICKETS</p>
  <p class="presale-url">WWW.KUPPELFEST.EXAMPLE</p>
</main>
</body>
</html>
```